menu for prepared meals company

Currently have a menu set up with company logo, would like something more eye catching and artistic to make it look professional. This is a fitness and health driven company in regards to purchasing prepared meals to use towards fitness goals. Do not necessarily want the menu to be geared towards muscular men and women. Looking to have the menu be simple to understand, exactly what it stands for, and geared towards a large demographic in health and life style eating changes.

Target Market(s)

health/fitness

Industry/Entity Type

It Company

Requirements
Must have
• *please see set up for mock menu and apply changes that were applied in the word document menu information.
• ex:do not offer sweet potato and chicken hash*

```html
<!DOCTYPE html>
<html lang="en">
<head>
<meta charset="utf-8">
<title>Fit Plate Kitchen — Menu</title>
<link rel="stylesheet" href="https://fonts.googleapis.com/css2?family=Questrial&display=swap">
<style>
:root{
  --red:#b5001b;
  --black:#0b0b0b;
  --white:#ffffff;
  --paper:#f4f4f4;
  --bg:#cfcfcf;
  --ink:#111111;
}
*{margin:0;padding:0;box-sizing:border-box}
html,body{width:1200px;height:780px;overflow:hidden}
body{background:radial-gradient(circle at 50% 40%,#e2e2e2,var(--bg));font-family:"Questrial",sans-serif;color:var(--ink);position:relative}
.menu{position:absolute;left:60px;top:80px;width:1080px;height:620px;display:flex;box-shadow:0 14px 40px rgba(0,0,0,.28)}
.panel{position:relative;width:360px;height:620px;background:var(--white);overflow:hidden}
.panel + .panel{border-left:1px solid #e4e4e4}
.abs{position:absolute}
.red{background:var(--red);color:var(--white)}
.black{background:var(--black);color:var(--white)}

/* cover */
.cover .band-top{left:0;top:0;width:100%;height:50px}
.cover .band-bottom{left:0;bottom:0;width:100%;height:50px}
.brand{left:0;top:180px;width:100%;display:flex;align-items:center;justify-content:center;gap:12px;color:var(--red);font-size:34px;line-height:1}
.brand-dot{width:14px;height:14px;border-radius:50%;background:var(--red)}
.menu-band{left:0;top:400px;width:100%;height:86px;display:flex;align-items:center;justify-content:center;font-size:54px;letter-spacing:22px;padding-left:22px}

/* specialty */
.specialty{left:0;top:50px;width:100%;height:250px;text-align:center;padding:16px 18px 0}
.specialty h2{font-weight:400;font-size:27px;letter-spacing:.5px;margin-bottom:10px}
.dish{margin-bottom:9px}
.dish h3{font-weight:400;font-size:15px;letter-spacing:.3px}
.dish p{font-size:10px;line-height:1.25;opacity:.92}
.price-box{left:200px;top:300px;width:160px;height:210px;text-align:center;padding-top:20px;font-size:18px;line-height:1.25}
.price-box .price{font-size:30px;margin-top:4px}
.delivery{left:0;top:510px;width:100%;height:74px;display:flex;align-items:center;justify-content:space-between;padding:0 22px}
.delivery p{font-size:15px;text-align:center;line-height:1.2}
.ph-round{width:50px;height:50px;border-radius:50%;background:rgba(255,255,255,.85)}

/* build your own */
.right .band-top{left:0;top:0;width:100%;height:40px}
.create{left:0;top:40px;width:100px;height:140px;text-align:center;padding-top:14px}
.create h3{font-weight:400;font-size:19px;line-height:1}
.create small{display:block;font-size:10px;margin-top:8px}
.containers{display:flex;justify-content:center;gap:16px;margin-top:8px}
.container{display:flex;flex-direction:column;align-items:center;font-size:7px}
.container i{display:flex;align-items:center;justify-content:center;width:20px;height:24px;border:2px solid var(--white);border-radius:3px;font-style:normal;font-size:7px;margin-bottom:2px}
.price-list{list-style:none;font-size:12.5px}
.price-list li{display:flex;justify-content:space-between;height:25px;align-items:center}
.price-list .amt{color:var(--red)}
.proteins{left:112px;top:46px;width:236px}
.fish{left:0;top:180px;width:215px;height:100px;padding:6px 14px 0}
.fish .price-list .amt{color:var(--white)}
.fish .price-list li{height:22px;font-size:12px}
.fish-note{left:215px;top:180px;width:145px;height:100px;text-align:center;padding-top:8px;font-size:13px;line-height:1.1}
.ph-fish{width:58px;height:34px;margin:8px auto 0;border-radius:50% 40% 40% 50%;background:rgba(255,255,255,.85)}
.icon-col{left:0;top:280px;width:40px;height:220px;display:flex;flex-direction:column;align-items:center;justify-content:space-around;padding:8px 0}
.ph-icon{width:26px;height:26px;border-radius:6px;background:rgba(255,255,255,.85)}
.choices{left:40px;top:280px;width:320px;height:220px;display:flex;padding:14px 10px 0 18px}
.choices .col{flex:1;text-align:center}
.choices h3{color:var(--red);font-weight:400;font-size:18px;line-height:1.1;margin-bottom:10px}
.choices ul{list-style:none;font-size:12.5px;line-height:26px}
.portion{left:40px;top:474px;width:320px;display:flex;justify-content:space-around;color:var(--red);font-size:12px}
.combo-note{left:0;top:500px;width:250px;height:70px;display:flex;align-items:center;justify-content:center;text-align:center;font-size:10px;line-height:1.3;padding:0 18px}
.also{left:250px;top:500px;width:110px;height:70px;display:flex;align-items:center;justify-content:center;text-align:center;font-size:11px;line-height:1.3;padding:0 10px}
</style>
</head>
<body>
<main class="menu">
  <section class="panel cover">
    <div class="abs black band-top"></div>
    <div class="abs brand"><span class="brand-dot"></span><span>Fit Plate Kitchen</span></div>
    <div class="abs red menu-band">MENU</div>
    <div class="abs black band-bottom"></div>
  </section>

  <section class="panel inside-left">
    <div class="abs red specialty">
      <h2>Specialty Meals</h2>
      <div class="dish"><h3>Pasta with Turkey Meatballs</h3><p>Whole grain pasta with turkey meatballs<br>and a tomato sauce</p></div>
      <div class="dish"><h3>Stir fry</h3><p>Chicken, stir fry vegetable mix<br>with jasmine rice</p></div>
      <div class="dish"><h3>Turkey burger</h3><p>Turkey Patty on a multigrain flat bread<br>with side of sweet potato fries</p></div>
      <div class="dish"><h3>Stuffed Pepper</h3><p>Pepper stuffed with ground turkey,<br>your choice of whole grain<br>or jasmine rice combined in a red sauce</p></div>
    </div>
    <div class="abs black price-box">
      <svg width="60" height="30" viewBox="0 0 60 30" aria-hidden="true">
        <g fill="none" stroke="#fff" stroke-width="2.5" stroke-linecap="round">
          <line x1="8" y1="4" x2="8" y2="28"/><line x1="4" y1="4" x2="4" y2="11"/><line x1="12" y1="4" x2="12" y2="11"/><path d="M4 11 Q8 15 12 11"/>
          <circle cx="30" cy="16" r="11"/><circle cx="30" cy="16" r="6"/>
          <path d="M52 28 V4 Q46 10 48 18 H52"/>
        </g>
      </svg>
      <p>All<br>specialty<br>Meals<br>are</p>
      <p class="price">$9.95</p>
    </div>
    <div class="abs red delivery">
      <div class="ph-round" role="img" aria-label="Customer service headset icon"></div>
      <p>Ofer at home<br>or delivery<br>within 20 miles<br>for small fee</p>
      <svg width="66" height="44" viewBox="0 0 66 44" aria-label="Delivery truck icon" role="img">
        <g fill="#fff"><rect x="2" y="4" width="38" height="26"/><path d="M42 12 H54 L64 22 V32 H42 Z"/></g>
        <g fill="var(--red)" stroke="#fff" stroke-width="3"><circle cx="14" cy="34" r="6"/><circle cx="52" cy="34" r="6"/></g>
      </svg>
    </div>
  </section>

  <section class="panel right">
    <div class="abs black band-top"></div>
    <div class="abs red create">
      <h3>Create<br>your<br>own</h3>
      <small>Choose protein</small>
      <div class="containers">
        <div class="container"><i>4oz</i>Half Size</div>
        <div class="container"><i>8oz</i>Full Size</div>
      </div>
    </div>
    <ul class="abs price-list proteins">
      <li><span>Chicken</span><span class="amt">7.95/8.95</span></li>
      <li><span>Ground Beef</span><span class="amt">7.95/8.95</span></li>
      <li><span>Ground Turkey</span><span class="amt">7.95/8.95</span></li>
      <li><span>Steak</span><span class="amt">9.95/10.95</span></li>
      <li><span>Turkey Tenderloin</span><span class="amt">7.95/8.95</span></li>
    </ul>
    <div class="abs black fish">
      <ul class="price-list">
        <li><span>Salmon</span><span class="amt">11.95</span></li>
        <li><span>Tilapia</span><span class="amt">10.95</span></li>
        <li><span>Cod</span><span class="amt">9.95</span></li>
        <li><span>Veggie Burger</span><span class="amt">9.95</span></li>
      </ul>
    </div>
    <div class="abs red fish-note">All<br>fish portions<br>are 6oz.
      <div class="ph-fish" role="img" aria-label="Fish icon"></div>
    </div>
    <div class="abs red icon-col">
      <div class="ph-icon" role="img" aria-label="Broccoli icon"></div>
      <div class="ph-icon" role="img" aria-label="Bowl of pasta icon"></div>
      <div class="ph-icon" role="img" aria-label="Pea pod icon"></div>
    </div>
    <div class="abs choices">
      <div class="col"><h3>Vegetables<br>Choices</h3><ul><li>Green Beans</li><li>Broccoli</li><li>Spinach</li><li>Asparagus</li></ul></div>
      <div class="col"><h3>Carb<br>Choices</h3><ul><li>Whole Grain Pasta</li><li>Whole Grain Rice</li><li>Jasmine Rice</li><li>Sweet potato</li></ul></div>
    </div>
    <div class="abs portion"><span>Half Size = 1/2 cup</span><span>Full Size = 1 cup</span></div>
    <div class="abs black combo-note">If two vegetable options are wanted they may choose two for low carb meal combo.</div>
    <div class="abs red also">Also available as combo</div>
  </section>
</main>
</body>
</html>
```